Ganzheitliche, gewaltfreie Hundeschule/ -betreuung sucht Flyer A6
Zielgruppe
Ich habe kürzlich die Hundetrainerausbildung abgeschlossen und möchte gerne als Hundesitter und Hundetrainerin durchstarten ;-)
Zur Kundengewinnung möchte ich gerne Flyer im Postkartenformat A6 quer auflegen/verteilen.
Da ich einerseits nur Einzelspaziergänge durchführe (keine Hundegruppe) bzw. nur Einzellektionen anbiete (keine Gruppenkurse) und ich andererseits als Hundesitter besser qualifiziert bin als der Durchschnitt, sind meine Preise etwas höher. Deshalb wird meine inskünftige Kundengruppe wohl aus der Mittelschicht kommen.
Das Design sollte wenn möglich Jung und Alt, weiblich und männlich, ansprechen.
Wichtig ist mir, dass mit dem Design hauptsächlich Menschen angesprochen werden, welche eine ähnliche Einstellung von Hundeerziehung haben - also absolut gewaltfrei. Oder andersrum: Leute, welche ihren Hund nur zum Statussymbol oder Befehlsempfänger degradieren, sollen nicht angesprochen werden bzw. würden von mir auch abgewiesen, weil sie bei mir nicht glücklich würden ;-)
Aufgabenstellung
Format: DIN A6 quer (Postkarte)
Vorderseite: süsser, selbstbewusster Hund,
sei es Foto (z.B. Mischlingshund) oder
Comic (z.B. "Sternflieger-Hund" Fiffo-Hund, aber nicht kindisch) oder
Gemälde (z.B. Castellini "Der Morgen des Fischers/Hunds) ;-)
sowie ein Hinweis zu meinem Angebot w.z.B. "Hundesitter gesucht? Hundeschule gesucht?" oder ähnlich
Vielleicht hat auch noch "respektvoll. ruhig. natürlich." irgendwo Platz.
Hinterseite:
Angebot:
-Einzelspaziergang Stadt Zürich und Adliswil
-Hundeschule Einzellektionen
Kontakt:
Schriftliche Anfragen (Mail, SMS, Kontaktformular) bevorzugt, vielen Dank.
Es wäre toll, wenn mein Logo (siehe Anhang) auch noch irgendwo Platz finden würde.
Vielleicht hat auch noch mein Slogan irgendwo Platz.
Die Postkarte sollte jung und modisch aussehen, aber auch vertrauenswürdig. Es sollte also nicht "zusammengebastelt" oder wie von mir selber gezeichnet aussehen sondern professionell.
Farben: warme, erdene Töne wie dunkelbraun, orange etc. Kein Pink, Blau etc.
Die fertige Version sollte ein HighEnd-pdf als Druckdatei sein, gerne können aber auch noch die offenen Daten mitgeliefert werden.

```html
<!DOCTYPE html>
<html lang="de">
<head>
<meta charset="utf-8">
<title>Pfotenweg – Flyer A6</title>
<link href="https://fonts.googleapis.com/css2?family=Jura:wght@400;600&family=Oswald:wght@500&family=Arimo:wght@400;700&display=swap" rel="stylesheet">
<style>
  :root {
    --bg: #ecebea;
    --paper: #ffffff;
    --orange: #f07d0a;
    --orange-light: #f9a23a;
    --brown: #2f211b;
    --brown-mid: #4a3128;
    --yellow: #ffc21a;
    --text: #3a2a22;
  }
  * { box-sizing: border-box; margin: 0; padding: 0; }
  html, body { width: 1200px; height: 1200px; overflow: hidden; background: var(--bg); }
  .sheet { position: relative; width: 1200px; height: 1200px; display: flex; align-items: center; justify-content: center; gap: 30px; }
  .card { position: relative; width: 555px; height: 392px; background: var(--paper); overflow: hidden; box-shadow: 0 6px 18px rgba(0,0,0,.22); font-family: "Arimo", sans-serif; color: var(--text); }

  .band { position: absolute; background: linear-gradient(90deg, var(--orange) 0%, var(--orange-light) 100%); color: #fff; font-family: "Jura", sans-serif; font-weight: 600; }
  .headline { font-variant: small-caps; letter-spacing: .5px; }

  .brand-mark { position: absolute; border-radius: 50%; background: radial-gradient(circle at 50% 45%, var(--yellow) 0%, var(--orange) 75%); box-shadow: 0 0 0 8px var(--paper); }
  .brand-name { position: absolute; width: 170px; text-align: center; white-space: nowrap; font-family: "Jura", sans-serif; font-weight: 600; color: var(--brown); font-size: 24px; line-height: 28px; }

  .photo { position: absolute; background: radial-gradient(ellipse at 50% 45%, #d9b58c 0%, #c79a6c 45%, #f3ebe2 80%, #ffffff 100%); }

  .footer { position: absolute; left: 0; bottom: 0; width: 100%; }
  .footer svg { display: block; }
  .footer-text { position: absolute; left: 0; bottom: 0; width: 100%; font-family: "Oswald", sans-serif; font-weight: 500; text-transform: uppercase; white-space: nowrap; }

  /* Front */
  .front .band-title { left: 0; top: 44px; width: 450px; height: 38px; padding-left: 20px; font-size: 27px; line-height: 38px; }
  .front .brand-mark { left: 410px; top: 22px; width: 90px; height: 90px; }
  .front .brand-name { left: 370px; top: 124px; }
  .offer-tag { position: absolute; left: 0; top: 88px; width: 395px; height: 32px; background: var(--brown); clip-path: polygon(0 0, 100% 0, 96% 100%, 0 100%); color: #fff; font-family: "Jura", sans-serif; font-weight: 600; font-size: 15px; line-height: 32px; padding-left: 20px; font-variant: small-caps; white-space: nowrap; }
  .offer-tag .accent { color: var(--orange-light); }
  .front .photo { left: 100px; top: 128px; width: 265px; height: 220px; }
  .phone-badge { position: absolute; left: 10px; top: 212px; width: 108px; height: 108px; border-radius: 50%; background: radial-gradient(circle at 40% 30%, var(--brown-mid), var(--brown)); box-shadow: 0 0 0 4px #fff, 0 3px 8px rgba(0,0,0,.35); color: #fff; text-align: center; padding-top: 22px; }
  .phone-badge .label { font-size: 13px; }
  .phone-badge .number { font-size: 14px; font-weight: 700; margin: 2px 0 3px; white-space: nowrap; }
  .phone-badge .note { font-size: 8px; line-height: 1.25; color: #e8ddd6; }
  .front .footer-text { height: 36px; padding-left: 20px; font-size: 20px; line-height: 36px; color: var(--orange); letter-spacing: 1.5px; }

  /* Back */
  .back .brand-mark { left: 36px; top: 30px; width: 90px; height: 90px; }
  .back .brand-name { left: -4px; top: 132px; }
  .back .band-title { left: 150px; top: 52px; right: 0; height: 58px; padding-left: 22px; padding-top: 6px; }
  .back .band-title .name { font-size: 27px; line-height: 28px; display: block; }
  .back .band-title .slogan { font-size: 14px; font-weight: 400; display: block; }
  .contact { position: absolute; left: 60px; top: 176px; width: 185px; font-size: 11px; line-height: 1.55; }
  .contact .title { font-family: "Jura", sans-serif; font-weight: 600; font-variant: small-caps; color: var(--orange); font-size: 15px; }
  .contact ul { list-style: none; }
  .contact li { display: flex; align-items: center; gap: 6px; white-space: nowrap; }
  .contact li svg { width: 11px; height: 11px; flex: none; }
  .contact .person { margin-left: 17px; }
  .contact .remark { margin-top: 8px; font-size: 7.5px; line-height: 1.35; }
  .back .photo { left: 255px; top: 112px; width: 300px; height: 225px; }
  .back .footer-text { height: 34px; text-align: center; font-size: 13px; line-height: 34px; color: #fff; letter-spacing: .5px; }
  .back .footer-text .url { color: var(--yellow); }
</style>
</head>
<body>
<main class="sheet">

  <section class="card front">
    <div class="band band-title headline">Hundesitter gesucht?</div>
    <div class="offer-tag"><span class="accent">Einzelspaziergang</span> Stadt Zürich und Aduswil</div>
    <div class="brand-mark"></div>
    <div class="brand-name">Pfotenweg.ch</div>
    <div class="photo" role="img" aria-label="Foto: lächelnder Mischlingshund mit Kette, liegend, daneben eine Lederleine"></div>
    <div class="footer">
      <svg width="555" height="62" viewBox="0 0 555 62" aria-hidden="true">
        <path d="M0 18 Q280 30 555 2 L555 62 L0 62 Z" fill="var(--brown)"/>
        <path d="M0 16 Q280 28 555 0" fill="none" stroke="var(--orange)" stroke-width="3"/>
      </svg>
      <div class="footer-text">"Respektvoll. Ruhig. Natürlich."</div>
    </div>
    <div class="phone-badge">
      <div class="label">Telefon:</div>
      <div class="number">079 555 18 27</div>
      <div class="note">( gerne auch Anfragen<br>schriftlich per E-Mail )</div>
    </div>
  </section>

  <section class="card back">
    <div class="band band-title headline">
      <span class="name">Pfotenweg...</span>
      <span class="slogan">und du wirst ein bisschen Hund</span>
    </div>
    <div class="brand-mark"></div>
    <div class="brand-name">Pfotenweg.ch</div>
    <div class="contact">
      <div class="title">Kontakt:</div>
      <div class="person">Nora Kessler</div>
      <ul>
        <li>
          <svg viewBox="0 0 12 12"><rect x="1" y="2.5" width="10" height="7" fill="none" stroke="var(--orange)" stroke-width="1.2"/><path d="M1 2.5 L6 6.5 L11 2.5" fill="none" stroke="var(--orange)" stroke-width="1.2"/></svg>
          kontakt@pfotenweg-mail.ch
        </li>
        <li>
          <svg viewBox="0 0 12 12"><circle cx="6" cy="6" r="5" fill="none" stroke="var(--orange)" stroke-width="1.2"/><path d="M1 6 H11 M6 1 Q2.5 6 6 11 M6 1 Q9.5 6 6 11" fill="none" stroke="var(--orange)" stroke-width="1"/></svg>
          www.pfotenweg.ch
        </li>
        <li>
          <svg viewBox="0 0 12 12"><path d="M2 4 Q2 2 4 2 H8 Q10 2 10 4 V5 H8 V4 H4 V5 H2 Z M3 6 H9 L10 10 H2 Z" fill="var(--orange)"/></svg>
          079 555 18 27
        </li>
      </ul>
      <p class="remark">Schriftliche Anfragen (Mail, SMS,<br>Kontaktformular) bevorzugt, vielen<br>Dank.</p>
    </div>
    <div class="photo" role="img" aria-label="Foto: junger Jack-Russell-Terrier, der neugierig in die Kamera schaut"></div>
    <div class="footer">
      <svg width="555" height="56" viewBox="0 0 555 56" aria-hidden="true">
        <path d="M0 14 Q280 26 555 4 L555 56 L0 56 Z" fill="var(--brown)"/>
        <path d="M0 12 Q280 24 555 2" fill="none" stroke="var(--orange)" stroke-width="2.5"/>
      </svg>
      <div class="footer-text">Alle Preise, sowie aktuelle Angebote finden Sie unter <span class="url">www.pfotenweg.ch</span></div>
    </div>
  </section>

</main>
</body>
</html>
```